Web Design for One for One Organic Soap Company

We need a website design for the company Tidewell Botanics based on the package design per attached.

The design should communicate high end, luxury organic. The site will provide facts about how the spread of disease causes deaths and can be prevented with hand washing. The site will also have a page about why we are passionate about organics and how that relates to our skin including skin facts.
Also, the site should have an e-commerce product page and shopping cart.

Target Market(s)

Educated, health conscious and socially conscious consumers who shop luxury. Target vendors include Larkmont Grocers and Velbrook..

Industry/Entity Type

E-Commerce

Font styles to use
Other font styles liked:
• See attached

Requirements
Must have
• Use of Ying Yang leaf Logo provided.
Based on design provided.

```html
<!DOCTYPE html>
<html lang="en">
<head>
<meta charset="utf-8">
<title>Tidewell Botanics — Organic Soap</title>
<link rel="stylesheet" href="https://fonts.googleapis.com/css2?family=Yanone+Kaffeesatz:wght@300;400&family=Open+Sans:ital,wght@0,400;0,600;1,700&display=swap">
<style>
:root{
  --tan:#ceb08e;
  --tan-light:#e6d3bb;
  --brown:#5a4030;
  --brown-dark:#3d2818;
  --rust:#a63a22;
  --ink:#3a2a1e;
  --text:#4a4a4a;
  --white:#ffffff;
  --frame:#efe7dd;
}
*{margin:0;padding:0;box-sizing:border-box}
html,body{width:1093px;height:1200px;overflow:hidden;background:var(--white)}
body{position:relative;font-family:"Open Sans",sans-serif;color:var(--text)}
.cond{font-family:"Yanone Kaffeesatz",sans-serif}
.abs{position:absolute}

/* header */
.site-header{left:0;top:0;width:1093px;height:106px;background:var(--tan);box-shadow:0 2px 4px rgba(0,0,0,.15);z-index:2}
.brand{left:143px;top:28px;display:flex;align-items:center;gap:10px}
.brand-mark{width:44px;height:64px;background:var(--rust)}
.brand-name{font-family:"Yanone Kaffeesatz",sans-serif;font-weight:400;font-size:30px;color:var(--brown-dark);line-height:1}
.account-links{right:176px;top:24px;font-family:"Yanone Kaffeesatz",sans-serif;font-size:16px;color:var(--ink)}
.account-links .login{color:var(--rust)}
.account-links .sep{margin:0 6px}
.main-nav{left:498px;top:64px;display:flex;height:26px;font-family:"Yanone Kaffeesatz",sans-serif;font-size:17px;color:var(--ink)}
.main-nav a{color:inherit;text-decoration:none;line-height:26px;padding:0 12px}
.main-nav a.current{background:var(--brown);color:var(--white);padding:0 16px}
.search{left:762px;top:64px;width:157px;height:26px;background:#f4eee6;font-family:"Yanone Kaffeesatz",sans-serif;font-size:15px;color:#555;line-height:26px;padding-left:8px}
.search svg{position:absolute;right:8px;top:5px}

/* hero */
.hero{left:0;top:106px;width:1093px;height:372px;background:linear-gradient(90deg,#fbf8f4 0%,#f5ede4 45%,#ecdfd3 100%)}
.hero-scene{left:430px;top:106px;width:663px;height:372px;background:linear-gradient(135deg,#e9c7bd 0%,#f1e6e0 50%,#b9cf95 100%)}
.hero-tag{left:143px;height:33px;background:var(--brown-dark);color:var(--white);font-family:"Yanone Kaffeesatz",sans-serif;font-weight:300;font-size:23px;line-height:33px;padding:0 11px}
.hero-pack{left:143px;top:294px;width:193px;height:150px;background:linear-gradient(160deg,#c4995a,#8a6436);box-shadow:-6px 10px 14px rgba(0,0,0,.3)}
.slider-dots{left:492px;top:495px;width:98px;height:26px;border-radius:13px;background:#fff;box-shadow:0 3px 6px rgba(0,0,0,.18);display:flex;justify-content:center;align-items:center;gap:8px}
.slider-dots span{width:12px;height:12px;border-radius:50%;border:1px solid #bbb;background:#f4f4f4}
.slider-dots span.on{background:var(--tan);border-color:#b89a74}

/* products */
.section-tab{left:470px;top:592px;width:151px;height:43px;background:var(--brown);color:var(--white);font-family:"Yanone Kaffeesatz",sans-serif;font-size:20px;text-align:center;line-height:43px}
.products{left:143px;top:635px;width:802px;height:214px;background:var(--tan);border-radius:2px}
.arrow{top:721px;width:34px;height:47px;background:var(--brown);display:flex;align-items:center;justify-content:center}
.product{top:669px;width:187px;text-align:center}
.product-photo{height:121px;border:4px solid var(--frame)}
.product-name{margin-top:15px;font-size:16px;color:var(--ink)}

/* why */
.why-title{left:0;top:902px;width:1093px;text-align:center;font-family:"Yanone Kaffeesatz",sans-serif;font-size:19px;color:var(--ink)}
.why-title span{border-bottom:1px solid var(--ink);padding-bottom:1px}
.why-copy{left:240px;top:940px;width:613px;text-align:center;font-size:12px;line-height:19.2px;color:var(--text)}
.btn{left:506px;top:1026px;width:91px;height:32px;background:var(--brown);color:var(--white);font-size:12px;font-weight:700;font-style:italic;text-align:center;line-height:32px;border-radius:1px}

/* footer */
.site-footer{left:0;top:1111px;width:1093px;height:89px;background:var(--brown-dark);border-top:3px solid #5c4431;text-align:center;font-size:11px;color:#c9b49a}
.footer-nav{margin-top:21px}
.footer-nav a{color:inherit;text-decoration:none}
.footer-nav a.current{color:var(--white)}
.footer-nav .sep{margin:0 10px}
.copyright{margin-top:8px}
</style>
</head>
<body>

<header class="site-header abs">
  <div class="brand abs">
    <span class="brand-mark"></span>
    <span class="brand-name">Tidewell Botanics</span>
  </div>
  <div class="account-links abs">
    <span class="login">Login</span><span class="sep">|</span>Register<span class="sep">|</span>Shopping Cart : 0
  </div>
  <nav class="main-nav abs">
    <a class="current" href="#">Home</a>
    <a href="#">About Us</a>
    <a href="#">Products</a>
    <a href="#">Contacts</a>
  </nav>
  <div class="search abs">Search here
    <svg width="16" height="16" viewBox="0 0 16 16"><circle cx="6.5" cy="6.5" r="5" fill="none" stroke="#6a7a8a" stroke-width="1.5"/><line x1="10" y1="10" x2="15" y2="15" stroke="#6a7a8a" stroke-width="2"/></svg>
  </div>
</header>

<section class="hero abs"></section>
<div class="hero-scene abs" role="img" aria-label="Folded pink and white towels with a perfume bottle, a green bath bomb and a bar of green soap"></div>
<div class="hero-tag abs" style="top:213px">Go for Organic Soap</div>
<div class="hero-tag abs" style="top:252px">&amp; Keep away from disease</div>
<div class="hero-pack abs" role="img" aria-label="Kraft-paper soap box with the brand label"></div>
<div class="slider-dots abs"><span class="on"></span><span></span><span></span><span></span></div>

<div class="section-tab abs">OUR PRODUCTS</div>
<section class="products abs"></section>
<div class="arrow abs" style="left:143px"><svg width="14" height="24" viewBox="0 0 14 24"><polyline points="12,2 2,12 12,22" fill="none" stroke="#fff" stroke-width="1.6"/></svg></div>
<div class="arrow abs" style="left:911px"><svg width="14" height="24" viewBox="0 0 14 24"><polyline points="2,2 12,12 2,22" fill="none" stroke="#fff" stroke-width="1.6"/></svg></div>

<div class="product abs" style="left:220px">
  <div class="product-photo" role="img" aria-label="Stacked bars of lavender soap" style="background:linear-gradient(135deg,#8d8494,#5e5666)"></div>
  <div class="product-name">Lavender Soap</div>
</div>
<div class="product abs" style="left:456px">
  <div class="product-photo" role="img" aria-label="Cut blocks of lemongrass tea soap" style="background:linear-gradient(135deg,#d8d27a,#bdb650)"></div>
  <div class="product-name">Emongrasstea Soap</div>
</div>
<div class="product abs" style="left:689px">
  <div class="product-photo" role="img" aria-label="Clove soap bars with rosemary and lavender sprigs" style="background:linear-gradient(135deg,#f1ebe2,#d9c4a4 60%,#7a6388)"></div>
  <div class="product-name">Soapclove</div>
</div>

<h2 class="why-title abs"><span>WHU YOU SHOULD USE ORGANIC SOAP</span></h2>
<p class="why-copy abs">The site will provide facts about how the spread of disease causes deaths and can be prevented with hand washing. The site will also have a page about why we are passionate about organics and<br>how that relates to our skin including skin facts.</p>
<div class="btn abs">Know More</div>

<footer class="site-footer abs">
  <div class="footer-nav">
    <a class="current" href="#">Home</a><span class="sep">|</span><a href="#">About Us</a><span class="sep">|</span><a href="#">Products</a><span class="sep">|</span><a href="#">Contacts</a><span class="sep">|</span><a href="#">Privacy Policy</a>
  </div>
  <div class="copyright">Copyright@2014, Tidewell Botanics</div>
</footer>

</body>
</html>
```